Construction proffessionals servicing the inner suburbs of Melbournes NorthWest specialising in aler

I would like a web site that is sharp, contemporary and simple to navigate, ie.not too many pages. i would like a home page with some info about us, who we are what our history is and my passion for building and construction based on impeccable customer focus. i would like a projects page and somewhere for clients to add testimonials. i would like a project calculator as well so prospective clients can work out a rough budget prior to contacting. i would like the colours to be in line with my logo which i have uploaded. i have many photos which can be used and can be shared via drop box when required. I would like it to be personal to capture our transparent process. i would like to add our company process as well. be brave and take risks.

Target Market(s)

People renovating and extending their homes, people needing inspections on new homes and pre-purchase inspections

Industry/Entity Type

Construction

Number of Pages Required

5+ page

Requirements
Must have
• Professional, easy to navigate, provide viewers with a happy experience, look great, contacts, project calculator, link through to my training company www.ktrp.vic.edu.au also check ormwaybuilds on instagram for pics
Nice to have
• Links to instagram, fonts to match email signature

```html
<!DOCTYPE html>
<html lang="en">
<head>
<meta charset="utf-8">
<title>Ormway Group – Construction Professionals</title>
<link href="https://fonts.googleapis.com/css2?family=Open+Sans:wght@400;600;700&display=swap" rel="stylesheet">
<style>
:root{
  --orange:#f5a623;
  --orange-dark:#e08e0b;
  --charcoal:#4b4b4b;
  --slate:#5e5e5e;
  --panel:#6a6a6a;
  --light:#f2f2f2;
  --white:#ffffff;
  --text:#555555;
}
*{box-sizing:border-box;margin:0;padding:0}
html,body{width:672px;height:1200px;overflow:hidden}
body{font-family:'Open Sans',Arial,sans-serif;background:var(--light);color:var(--text);font-size:7px;line-height:1.4;position:relative}

.site-header{height:62px;background:var(--white);position:relative}
.brand{position:absolute;left:40px;top:0;height:56px;padding:0 14px;background:var(--orange);display:flex;align-items:center;gap:8px}
.brand-mark{width:14px;height:14px;background:var(--white)}
.brand-name{font-weight:700;font-size:22px;color:var(--white);letter-spacing:1px}
.header-contact{position:absolute;right:46px;top:30px;display:flex;gap:18px;font-size:7px;color:var(--charcoal)}
.social-top{position:absolute;right:46px;top:10px;display:flex;gap:6px}
.social-top i{width:13px;height:13px;border-radius:50%;background:var(--orange);display:block}

.main-nav{height:16px;background:var(--charcoal);display:flex;padding-left:40px}
.main-nav a{color:var(--white);text-decoration:none;font-size:7px;padding:0 20px;line-height:16px}
.main-nav a.active{background:var(--orange)}

.hero{position:relative;height:300px;background:linear-gradient(100deg,#8c99a6 0%,#b9c0c6 35%,#d9b07a 60%,#6d6a66 100%)}
.hero-tagline{position:absolute;left:40px;top:110px;color:var(--white);font-weight:700;font-size:12px;line-height:1.25;width:260px;text-transform:uppercase}

.about{position:absolute;left:40px;top:336px;width:592px;height:104px;background:rgba(245,166,35,.92);color:var(--white);text-align:center;padding:14px 26px}
.about h2{font-size:13px;font-weight:600;margin-bottom:8px}
.about p{font-size:6.5px;line-height:1.6}

.section-title{font-size:13px;font-weight:600;color:var(--charcoal);padding-left:46px;display:flex;align-items:center;gap:10px}
.section-title::after{content:"";flex:1;height:1px;background:#cfcfcf;margin-right:46px}
.projects-title{position:absolute;top:454px;left:0;right:0}
.projects{position:absolute;top:490px;left:46px;width:580px;display:flex;gap:12px}
.project-card{flex:1;background:var(--white);box-shadow:0 1px 3px rgba(0,0,0,.15)}
.project-card .photo{height:70px;background:linear-gradient(160deg,#9aa7b3,#7b7f82 60%,#b09b7f)}
.project-card h3{font-size:7px;color:var(--orange-dark);font-weight:600;padding:10px 8px 6px}
.project-card ul{list-style:none;padding:0 8px 16px}
.project-card li{font-size:6.5px;margin-bottom:8px;display:flex;align-items:center;gap:4px;color:var(--charcoal)}
.project-card li::before{content:"";width:5px;height:5px;border-radius:50%;background:var(--orange)}

.calculator{position:absolute;top:732px;left:0;width:672px;height:134px;background:var(--slate);overflow:hidden}
.calculator .sketch{position:absolute;right:0;top:0;width:170px;height:134px;background:linear-gradient(120deg,#6c6c6c,#8a8a8a)}
.calculator svg{position:absolute;left:0;top:0}
.calculator .content{position:absolute;left:140px;top:24px;width:350px;color:var(--white)}
.calculator h2{font-size:13px;color:var(--orange);font-weight:600;margin-bottom:8px}
.calculator p{font-size:6.5px;line-height:1.6}

.method-title{position:absolute;top:894px;left:0;right:0}
.methods{position:absolute;top:930px;left:46px;width:580px;display:flex;gap:14px}
.method-card{flex:1;background:var(--panel);height:100px;display:flex;gap:8px;padding:12px 10px}
.method-card .icon{width:26px;height:26px;background:var(--orange);flex:none}
.method-card h3{font-size:7px;color:var(--orange);font-weight:600;margin-bottom:5px}
.method-card p{font-size:6.5px;color:var(--white);line-height:1.5}

.contact-strip{position:absolute;top:1054px;left:0;width:672px;height:44px;background:var(--orange);display:flex;padding:0 46px}
.contact-strip div{flex:1;color:var(--white);font-weight:600;font-size:8px;padding-top:8px}
.contact-strip div::after{content:"";display:block;width:9px;height:9px;background:var(--charcoal);margin-top:6px;margin-left:40px}
.footer{position:absolute;top:1098px;left:0;width:672px;height:82px;background:var(--charcoal);display:flex;padding:14px 46px}
.footer ul{flex:1;list-style:none}
.footer li{font-size:6px;color:#dcdcdc;margin-bottom:3px}
.follow h4{font-size:8px;color:var(--white);font-weight:600;margin-bottom:6px}
.follow .icons{display:flex;gap:5px}
.follow .icons i{width:14px;height:14px;background:#777;display:block}
.bottom-bar{position:absolute;top:1180px;left:0;width:672px;height:20px;background:#3a3a3a;color:#bbb;font-size:6px;display:flex;justify-content:space-between;align-items:center;padding:0 46px}
</style>
</head>
<body>
<header class="site-header">
  <div class="brand"><span class="brand-mark"></span><span class="brand-name">OWG</span></div>
  <div class="social-top"><i></i><i></i><i></i><i></i></div>
  <div class="header-contact">
    <span>28 Kestrel Lane, Vic 3041</span>
    <span>info@ormwaybuilds.com</span>
    <span>(03) 9412 7730</span>
  </div>
</header>
<nav class="main-nav">
  <a class="active">Home</a><a>About Us</a><a>Who We Are</a><a>Projects</a><a>Testimonials</a><a>Contact Us</a>
</nav>
<section class="hero" role="img" aria-label="Builder in hard hat on a construction site with an excavator">
  <p class="hero-tagline">Providing quality expert advice, common sense and friendly professional service</p>
</section>
<section class="about">
  <h2>About Ormway Group</h2>
  <p>We are a family owned building team servicing the inner north west of Melbourne, with a passion for alterations, extensions and honest home inspections. Our history is built on clear communication, careful planning and craftsmanship you can trust. From the first site visit to handover, every client is kept informed at each stage, and every job is treated as if it were our own home. Ask us about our training courses too.</p>
</section>

<h2 class="section-title projects-title">Our Projects</h2>
<div class="projects">
  <article class="project-card"><div class="photo" role="img" aria-label="Completed home extension"></div><h3>Brunswick Rear Extension</h3><ul><li>Open plan living area</li><li>New timber deck</li><li>Internal layout redesign</li><li>Finished in ten weeks</li></ul></article>
  <article class="project-card"><div class="photo" role="img" aria-label="Renovated street frontage"></div><h3>Coburg Full Renovation</h3><ul><li>Open plan living area</li><li>New timber deck</li><li>Internal layout redesign</li><li>Finished in ten weeks</li></ul></article>
  <article class="project-card"><div class="photo" role="img" aria-label="Building site under construction"></div><h3>Essendon Second Storey</h3><ul><li>Open plan living area</li><li>New timber deck</li><li>Internal layout redesign</li><li>Finished in ten weeks</li></ul></article>
  <article class="project-card"><div class="photo" role="img" aria-label="New home pre-handover"></div><h3>Pascoe Vale Inspection</h3><ul><li>Open plan living area</li><li>New timber deck</li><li>Internal layout redesign</li><li>Finished in ten weeks</li></ul></article>
</div>

<section class="calculator">
  <svg width="130" height="134" viewBox="0 0 130 134" aria-hidden="true"><polygon points="0,0 90,0 130,67 90,134 0,134" fill="#4b4b4b"/></svg>
  <div class="sketch" role="img" aria-label="Architectural sketch of a building frame"></div>
  <div class="content">
    <h2>Calculate Your Project Cost</h2>
    <p>Planning a renovation or extension? Enter a few details about your home and the work you have in mind, and our project calculator will give you a rough budget before you call us. It covers demolition, framing, finishes and inspections, so you can plan with confidence. Once you have an estimate, get in touch and we will walk through the numbers together on site.</p>
  </div>
</section>

<h2 class="section-title method-title">Project Methodology</h2>
<div class="methods">
  <div class="method-card"><span class="icon"></span><div><h3>Consulting, Listening and Planning</h3><p>We meet on site, listen to your goals and agree on a clear scope and budget.</p></div></div>
  <div class="method-card"><span class="icon"></span><div><h3>Estimating and Tendering</h3><p>You receive a transparent quote with every item listed and explained.</p></div></div>
  <div class="method-card"><span class="icon"></span><div><h3>Execution</h3><p>Our crew builds to plan, with weekly updates until final handover.</p></div></div>
</div>

<div class="contact-strip">
  <div>0400-318-2276</div><div>Talk to Us</div><div>info@ormwaybuilds.com</div><div>(03) 9412 7730</div>
</div>
<footer class="footer">
  <ul><li>Home extensions</li><li>Alterations</li><li>Pre-purchase inspections</li><li>New home inspections</li></ul>
  <ul><li>Our process</li><li>Recent projects</li><li>Client testimonials</li><li>Project calculator</li></ul>
  <ul><li>About us</li><li>Training</li><li>Careers</li><li>Contact us</li></ul>
  <div class="follow"><h4>Follow Us</h4><div class="icons"><i></i><i></i><i></i><i></i></div></div>
</footer>
<div class="bottom-bar"><span>Terms of Use | Privacy Policy</span><span>© Ormway Group. All Rights Reserved.</span></div>
</body>
</html>
```